ReadNest Learning App for Children with Dyslexia

Project Description:

We are seeking a talented UI/UX designer to create engaging and intuitive designs for Readnest, an innovative educational app designed to help children learn letters and words through a multisensory learning approach. The app aims to be particularly helpful for children with dyslexia, providing a supportive and interactive learning environment.

Key App Features & Design Requirements:

Account Creation Screen: Design a welcoming and straightforward sign-up page that allows users to register with their email or continue with Quorvix. The design should be clean, focusing on user-friendliness and accessibility, adhering to our terms of service and privacy policy.

Main Screen Design: The main screen should allocate at least 4/6 of its height to the interactive drawing area. It needs to display word prompts in both correct and scrambled orders and include options to "Show all Words," "Play all words," and a search function. The interface should be vibrant, engaging, and easy to navigate for children.

Profile Section: Create a user-friendly profile page that allows users to edit their profile image, name, username, email, links, and bio. The design should be clean and encourage user engagement.

NestStats Page: This section will display the user's learning progress, including rankings, a learning curve, and recently learned words. It should visually represent progress in a motivating and understandable way, suitable for a younger audience.

Visual and Auditory Feedback Implementation: Incorporate elements that support visual and auditory feedback, using dyslexia-friendly formats. This includes choosing appropriate colors, fonts, and auditory cues.

Accessibility and Customization Settings: Designs should include settings for adjusting visual contrast, font size, and the word list to accommodate individual preferences and needs.

Feel free to add more interactions and/or pages.

Design preferences:

Color Scheme: Use a bright, inviting color palette that stimulates learning and engagement without overwhelming the users.
Font Selection: Opt for fonts that are readable and accessible, particularly for users with dyslexia.
Icons and Graphics: Design custom icons and graphics that are cohesive with the app's theme and purpose. Illustrations should be simple, relatable, and supportive of the learning process.

Target Market(s)

Educational

Industry/Entity Type

Educational

Colors
0054AA
0677BA
7BADD7
CADEEF
E8F1F8
0094D4
00A9DD
6FCCEA
C7EBF8
E9F6FB

Requirements
Must have
• Educational app, a writing area, scoring and account management
Nice to have
• Statistics, Ranking Page, Settings and some nice visual features

```html
<!DOCTYPE html>
<html lang="en">
<head>
<meta charset="UTF-8">
<title>Readnest – App Screens</title>
<link href="https://fonts.googleapis.com/css2?family=Lexend:wght@400;600&family=Open+Sans:wght@400;600;700&display=swap" rel="stylesheet">
<style>
  :root{
    --page:#e8e8e8;
    --screen:#ffffff;
    --ink:#1c1c1c;
    --ink-soft:#4a4a4a;
    --muted:#8a8f96;
    --navy:#0054aa;
    --blue:#0677ba;
    --sky:#0094d4;
    --sky-light:#7badd7;
    --mist:#cadeef;
    --haze:#e8f1f8;
    --line:#e3e6ea;
  }
  *{box-sizing:border-box;margin:0;padding:0}
  html,body{width:1200px;height:780px;overflow:hidden}
  body{background:var(--page);font-family:"Open Sans",sans-serif;color:var(--ink);position:relative}
  .screen{position:absolute;background:var(--screen);border-radius:22px;overflow:hidden;box-shadow:0 10px 30px rgba(0,0,0,.08)}
  .abs{position:absolute}
  .status-time{position:absolute;font-size:7px;color:var(--ink)}
  .status-icons{position:absolute;width:34px;height:8px}
  .btn-primary{position:absolute;border-radius:14px;background:linear-gradient(90deg,var(--sky),var(--navy));color:#fff;font-weight:700;display:flex;align-items:center;justify-content:center}

  /* sign-up */
  .signup{left:240px;top:198px;width:185px;height:401px}
  .brand{left:0;width:100%;top:40px;text-align:center;font-family:"Lexend",sans-serif;font-weight:600;font-size:28px;letter-spacing:-.5px}
  .tagline{left:0;width:100%;top:74px;text-align:center;font-family:"Lexend",sans-serif;font-size:10.5px;color:var(--ink-soft)}
  .account-card{left:10px;top:110px;width:164px;height:213px;border-radius:10px;background:linear-gradient(160deg,#dfe9f3,#e8f0f7 55%,#d5e2ee)}
  .card-title{left:14px;top:16px;font-size:9.5px;font-weight:600}
  .card-sub{left:14px;top:34px;font-size:6.2px;color:var(--ink-soft)}
  .email-row{left:12px;top:60px;width:141px;height:17px;border-bottom:1px solid #b9c6d3;display:flex;align-items:center;gap:6px;font-size:7px;font-weight:600}
  .signup .btn-primary{left:12px;top:93px;width:141px;height:25px;font-size:8.5px}
  .or-line{left:0;width:100%;top:128px;text-align:center;font-size:8.5px;color:var(--ink-soft)}
  .btn-outline{left:12px;top:150px;width:141px;height:24px;border:1px solid var(--blue);border-radius:13px;display:flex;align-items:center;justify-content:center;gap:6px;color:var(--blue);font-weight:600;font-size:8.5px}
  .dot{width:9px;height:9px;border-radius:50%;background:var(--blue)}
  .terms{left:12px;top:183px;width:142px;font-size:5.4px;line-height:1.7;color:var(--muted)}
  .stationery-art{left:10px;top:329px;width:165px;height:62px;border-radius:8px;background:linear-gradient(90deg,#b9cbef,#f3c9bd 45%,#f5e4a6 70%,#f4f4f4)}

  /* main */
  .main{left:503px;top:173px;width:203px;height:441px}
  .backdrop-art{left:0;top:60px;width:100%;height:381px;background:radial-gradient(circle at 40% 70%,#eef3fb,#f8f6f2 60%,#fff)}
  .menu-icon{left:16px;top:32px;width:13px;height:10px}
  .screen-title{left:0;width:100%;top:30px;text-align:center;font-weight:600;font-size:11px;color:var(--ink-soft)}
  .points{left:150px;top:32px;font-size:8.5px;color:var(--ink-soft)}
  .draw-area{left:24px;top:70px;width:156px;height:142px;background:#fff;border:1px solid var(--line);border-radius:6px}
  .edit-btn{left:65px;top:59px;width:25px;height:25px;border-radius:3px;background:linear-gradient(180deg,var(--sky),var(--blue));display:flex;align-items:center;justify-content:center}
  .word-toggle{left:24px;top:227px;width:155px;height:26px;border:1px solid var(--blue);border-radius:4px;background:#fff;display:flex;align-items:center;font-size:7.8px}
  .toggle-off{flex:1;padding-left:6px;color:var(--ink-soft)}
  .toggle-on{width:76px;height:22px;margin-right:1px;border-radius:3px;background:var(--navy);color:#fff;display:flex;align-items:center;justify-content:center}
  .letter-tile{width:34px;height:34px;background:#fff;border-radius:3px;box-shadow:0 1px 4px rgba(0,0,0,.08);display:flex;align-items:center;justify-content:center;font-weight:700;font-size:9px}
  .main .btn-primary{left:24px;top:364px;width:155px;height:27px;font-size:9px}

  /* profile */
  .profile{left:785px;top:197px;width:186px;height:400px}
  .profile-bg{left:0;top:40px;width:100%;height:360px;background:linear-gradient(135deg,#f4f8fc,#fdfbf8 50%,#f6f3fa)}
  .back-btn{left:13px;top:25px;width:15px;height:15px;border-radius:50%;background:var(--blue);display:flex;align-items:center;justify-content:center}
  .profile-title{left:0;width:100%;top:25px;text-align:center;font-size:10px;font-weight:600}
  .avatar{left:52px;top:48px;width:80px;height:80px;border-radius:50%;border:1.5px solid var(--sky-light);background:radial-gradient(circle at 50% 40%,#8a7460,#4d5a3f 70%,#2f3a2a)}
  .avatar-caption{left:0;width:100%;top:129px;text-align:center;font-size:7px}
  .field-label{left:12px;font-size:8px;font-weight:600}
  .field{left:13px;width:160px;height:21px;border:1px solid var(--line);border-radius:3px;background:rgba(255,255,255,.85);font-size:6.6px;color:var(--ink-soft);display:flex;align-items:center;justify-content:space-between;padding:0 7px}
</style>
</head>
<body>

<!-- Sign-up screen -->
<section class="screen signup">
  <span class="status-time" style="left:24px;top:8px">9:30</span>
  <svg class="status-icons" style="left:140px;top:9px" viewBox="0 0 34 8"><rect x="0" y="5" width="1.5" height="3" fill="#1c1c1c"/><rect x="2.5" y="3.5" width="1.5" height="4.5" fill="#1c1c1c"/><rect x="5" y="2" width="1.5" height="6" fill="#1c1c1c"/><path d="M10 3.5a5 5 0 0 1 7 0M11.5 5a3 3 0 0 1 4 0" stroke="#1c1c1c" fill="none" stroke-width="1"/><circle cx="13.5" cy="7" r=".8" fill="#1c1c1c"/><rect x="20" y="1.5" width="11" height="5.5" rx="1" fill="#1c1c1c"/><rect x="31.5" y="3" width="1" height="2.5" fill="#1c1c1c"/></svg>
  <h1 class="abs brand">Readnest</h1>
  <p class="abs tagline">Learn letters and words</p>
  <div class="abs account-card">
    <h2 class="abs card-title">Create an Account</h2>
    <p class="abs card-sub">Enter your email to sign up for this app</p>
    <div class="abs email-row">
      <svg width="12" height="9" viewBox="0 0 12 9"><rect x=".5" y=".5" width="11" height="8" fill="none" stroke="#6b7480" stroke-width=".8"/><path d="M.5 .5 6 5l5.5-4.5" fill="none" stroke="#6b7480" stroke-width=".8"/></svg>
      Email
    </div>
    <div class="btn-primary">Sign up with email</div>
    <p class="abs or-line">or continue with</p>
    <div class="abs btn-outline"><span class="dot"></span>Quorvix</div>
    <p class="abs terms">By clicking continue, you agree to our and Terms of Service Privacy Policy</p>
  </div>
  <div class="abs stationery-art" role="img" aria-label="Illustration of a ruler, protractor and set square on a wavy line"></div>
</section>

<!-- Main screen -->
<section class="screen main">
  <div class="abs backdrop-art" role="img" aria-label="Faint background photo of colourful puzzle pieces"></div>
  <span class="status-time" style="left:26px;top:10px">9:30</span>
  <svg class="status-icons" style="left:157px;top:11px" viewBox="0 0 34 8"><rect x="0" y="5" width="1.5" height="3" fill="#1c1c1c"/><rect x="2.5" y="3.5" width="1.5" height="4.5" fill="#1c1c1c"/><rect x="5" y="2" width="1.5" height="6" fill="#1c1c1c"/><path d="M10 3.5a5 5 0 0 1 7 0M11.5 5a3 3 0 0 1 4 0" stroke="#1c1c1c" fill="none" stroke-width="1"/><circle cx="13.5" cy="7" r=".8" fill="#1c1c1c"/><rect x="20" y="1.5" width="11" height="5.5" rx="1" fill="#1c1c1c"/><rect x="31.5" y="3" width="1" height="2.5" fill="#1c1c1c"/></svg>
  <svg class="abs menu-icon" viewBox="0 0 13 10"><path d="M0 1h13M0 5h13M0 9h13" stroke="#0677ba" stroke-width="1.4"/></svg>
  <h2 class="abs screen-title">Main Screen</h2>
  <span class="abs points">16 Points</span>
  <div class="abs draw-area">
    <div class="abs edit-btn"><svg width="11" height="11" viewBox="0 0 11 11"><path d="M2 9l.6-2.4L7.5 1.7l1.8 1.8-4.9 4.9z" fill="#fff"/></svg></div>
  </div>
  <div class="abs word-toggle"><span class="toggle-off">Show all Words</span><span class="toggle-on">Play all words</span></div>
  <div class="abs letter-tile" style="left:34px;top:267px">c</div>
  <div class="abs letter-tile" style="left:85px;top:267px">t</div>
  <div class="abs letter-tile" style="left:135px;top:267px">b</div>
  <div class="abs letter-tile" style="left:34px;top:312px">a</div>
  <div class="abs letter-tile" style="left:85px;top:312px">•••</div>
  <div class="btn-primary">Show me the results</div>
</section>

<!-- Profile screen -->
<section class="screen profile">
  <div class="abs profile-bg" role="img" aria-label="Faint background photo of coloured pencils"></div>
  <span class="status-time" style="left:24px;top:8px">9:30</span>
  <svg class="status-icons" style="left:143px;top:9px" viewBox="0 0 34 8"><rect x="0" y="5" width="1.5" height="3" fill="#1c1c1c"/><rect x="2.5" y="3.5" width="1.5" height="4.5" fill="#1c1c1c"/><rect x="5" y="2" width="1.5" height="6" fill="#1c1c1c"/><path d="M10 3.5a5 5 0 0 1 7 0M11.5 5a3 3 0 0 1 4 0" stroke="#1c1c1c" fill="none" stroke-width="1"/><circle cx="13.5" cy="7" r=".8" fill="#1c1c1c"/><rect x="20" y="1.5" width="11" height="5.5" rx="1" fill="#1c1c1c"/><rect x="31.5" y="3" width="1" height="2.5" fill="#1c1c1c"/></svg>
  <div class="abs back-btn"><svg width="9" height="6" viewBox="0 0 9 6"><path d="M8.5 3H1M3.5.5 1 3l2.5 2.5" fill="none" stroke="#fff" stroke-width=".9"/></svg></div>
  <h2 class="abs profile-title">Profile</h2>
  <div class="abs avatar" role="img" aria-label="Profile photo of the user"></div>
  <p class="abs avatar-caption">Edit profile image</p>

  <label class="abs field-label" style="top:159px">Name</label>
  <div class="abs field" style="top:168px">Mara Quill</div>
  <label class="abs field-label" style="top:199px">Username</label>
  <div class="abs field" style="top:209px">@username</div>
  <label class="abs field-label" style="top:240px">Email</label>
  <div class="abs field" style="top:250px">name@example.org</div>
  <label class="abs field-label" style="top:281px">Links</label>
  <div class="abs field" style="top:291px">yoursite.example<svg width="6" height="4" viewBox="0 0 6 4"><path d="M.5.5 3 3 5.5.5" fill="none" stroke="#4a4a4a" stroke-width=".8"/></svg></div>
  <label class="abs field-label" style="top:321px">Bio</label>
  <div class="abs field" style="top:331px">A description of this user.</div>
</section>

</body>
</html>
```